High-end residential home builder needs a business card design

We need a new business card design for a small residential construction company based in Boise, Idaho. We specialize in building custom high-end homes and remodels, with a focus on great design and craftsmanship.

We would like to use our current logo, but open to new color suggestions.
Just looking for a clean, sharp, modern design that looks high-end.

Target Market(s)

Upscale clientele

Industry/Entity Type

Contractor

Contact Information for Business Card

Company: Stonefield Custom Builders
Name: Marcus Tilley
Phone number: 208 367 4120
Email: MarcusTilleySCB@mailbox-example.com
Website: Stonefieldcustombuilders-example.com

Font styles to use
Serif
Sans Serif

Requirements
Must have
• Company Logo
Company name
My name
My phone number
My email
Company website
Nice to have
• I have attached a few photos of cards that I really like.

```html
<!DOCTYPE html>
<html lang="en">
<head>
<meta charset="utf-8">
<title>Stonefield Custom Builders – Business Card</title>
<link rel="stylesheet" href="https://fonts.googleapis.com/css2?family=Montserrat:wght@300;400;500&display=swap">
<style>
  :root {
    --backdrop: #aeb2b3;
    --card: #2b2b2d;
    --edge: #e8921f;
    --accent: #e8921f;
    --ink-light: #f2f2f2;
    --emboss: #3b3b3e;
    --font-main: "Montserrat", sans-serif;
  }
  * { box-sizing: border-box; margin: 0; padding: 0; }
  html, body {
    width: 1200px; height: 880px; overflow: hidden;
    background: var(--backdrop);
    font-family: var(--font-main);
  }
  .canvas {
    width: 1200px; height: 880px;
    display: flex; flex-direction: column;
    align-items: center; justify-content: center; gap: 44px;
  }
  .card {
    width: 640px; height: 366px;
    background: var(--card);
    border-bottom: 4px solid var(--edge);
    border-radius: 2px;
    box-shadow: 0 10px 24px rgba(0,0,0,.22);
    position: relative;
  }
  /* Front: contact side */
  .card-front {
    display: flex; flex-direction: column; align-items: center;
    padding-top: 62px; text-align: center;
  }
  .brand-mark {
    display: flex; align-items: center; gap: 10px;
    color: var(--ink-light);
    font-size: 13px; font-weight: 400; letter-spacing: 3px;
    text-transform: uppercase;
  }
  .brand-square {
    width: 14px; height: 14px; border: 2px solid var(--ink-light);
  }
  .holder-name {
    margin-top: 34px;
    color: var(--accent);
    font-size: 26px; font-weight: 500; letter-spacing: 1px;
    text-transform: uppercase;
  }
  .divider {
    width: 26px; height: 3px; background: var(--accent);
    margin: 16px 0 14px;
  }
  .phone {
    color: var(--ink-light);
    font-size: 17px; font-weight: 300; letter-spacing: 1px;
  }
  .web-line {
    margin-top: 18px;
    color: var(--ink-light);
    font-size: 13px; font-weight: 300; letter-spacing: .3px;
  }
  .web-line .sep { margin: 0 8px; }
  /* Back: company side */
  .card-back {
    display: flex; align-items: center; justify-content: center;
  }
  .back-brand {
    display: flex; align-items: center; gap: 22px;
    color: var(--emboss);
    font-size: 24px; font-weight: 500; letter-spacing: 6px;
    text-transform: uppercase;
    line-height: 1.5;
  }
  .back-square {
    width: 70px; height: 70px; border: 3px solid var(--emboss);
    flex-shrink: 0;
  }
</style>
</head>
<body>
<main class="canvas">
  <section class="card card-back" aria-label="Card back">
    <div class="back-brand">
      <span class="back-square"></span>
      <span class="back-name">Stonefield<br>Custom Builders</span>
    </div>
  </section>

  <section class="card card-front" aria-label="Card front">
    <div class="brand-mark">
      <span class="brand-square"></span>
      <span>Stonefield Custom Builders</span>
    </div>
    <h1 class="holder-name">Marcus Tilley</h1>
    <div class="divider"></div>
    <p class="phone">208 367 4120</p>
    <p class="web-line">
      <span class="email">MarcusTilleySCB@mailbox-example.com</span><span class="sep">|</span><span class="site">Stonefieldcustombuilders-example.com</span>
    </p>
  </section>
</main>
</body>
</html>
```